Business Card Design Project

Business Card
We are rebranding with a new logo
Industry/Entity Type
Business
Contact Information for Business Card
Dennis Marlow +61 427581962 dennis@qovo.com.au P.O. Box 872 Kelvindale QLD 4309
Requirements
Must have
- Logo

```html
<!DOCTYPE html>
<html lang="en">
<head>
<meta charset="utf-8">
<title>Qovo International — Business Card</title>
<link rel="stylesheet" href="https://fonts.googleapis.com/css2?family=Roboto:wght@400;700&family=Satisfy&display=swap">
<style>
  :root {
    --page: #e6e6e6;
    --blue-deep: #034d6f;
    --blue-mid: #0a7fb3;
    --blue-bright: #04a3dd;
    --navy-text: #0c4a6e;
    --ink: #1c1c1c;
    --accent: #e2661c;
    --card-white: #f6f6f6;
    --white: #ffffff;
  }
  * { box-sizing: border-box; margin: 0; padding: 0; }
  html, body {
    width: 1200px; height: 576px; overflow: hidden;
    background: var(--page);
    font-family: "Roboto", Arial, sans-serif;
  }
  .canvas { position: relative; width: 1200px; height: 576px; }
  .card {
    position: absolute;
    width: 484px; height: 292px;
    border-radius: 14px;
    box-shadow: 0 3px 8px rgba(0,0,0,0.22);
    overflow: hidden;
  }
  .card--front {
    left: 82px; top: 139px;
    background: linear-gradient(90deg, var(--blue-deep) 0%, var(--blue-mid) 50%, var(--blue-bright) 100%);
  }
  .card--back { left: 602px; top: 138px; background: var(--card-white); }

  .brand {
    position: absolute;
    display: flex; align-items: center; gap: 8px;
    font-weight: 700; letter-spacing: 0.12em; text-transform: uppercase;
  }
  .brand__dot { width: 12px; height: 12px; border-radius: 50%; background: var(--accent); flex: none; }
  .brand__name { line-height: 1.05; }
  .card--front .brand {
    left: 0; right: 0; top: 118px; justify-content: center;
    color: var(--white); font-size: 22px;
  }
  .card--back .brand {
    right: 32px; bottom: 44px;
    color: var(--ink); font-size: 14px;
  }

  .holder { position: absolute; left: 24px; top: 38px; }
  .holder__name {
    font-family: "Satisfy", cursive;
    font-size: 27px; color: var(--navy-text); line-height: 1;
  }
  .holder__title { margin-top: 6px; font-size: 11.5px; color: var(--ink); }

  .contacts { position: absolute; left: 26px; top: 216px; list-style: none; }
  .contacts__item {
    display: flex; align-items: center; gap: 12px;
    font-size: 12px; color: var(--ink); height: 17px;
  }
  .contacts__icon { width: 11px; height: 11px; fill: var(--accent); flex: none; }
</style>
</head>
<body>
<main class="canvas">
  <section class="card card--front" aria-label="Card front">
    <div class="brand">
      <span class="brand__dot"></span>
      <span class="brand__name">Qovo International</span>
    </div>
  </section>

  <section class="card card--back" aria-label="Card back">
    <div class="holder">
      <p class="holder__name">Dennis Marlow</p>
      <p class="holder__title">Managing Director</p>
    </div>

    <ul class="contacts">
      <li class="contacts__item">
        <svg class="contacts__icon" viewBox="0 0 12 12" aria-hidden="true"><path d="M1 4.5c0-1.5 2-2.5 5-2.5s5 1 5 2.5v.7H8.6V4.1H3.4v1.1H1z M3 6h6l1.5 4.5h-9z"/></svg>
        <span>+61 427581962</span>
      </li>
      <li class="contacts__item">
        <svg class="contacts__icon" viewBox="0 0 12 12" aria-hidden="true"><path d="M0.5 2.5h11v7h-11z M1.5 3.3l4.5 3.4 4.5-3.4" stroke="#f6f6f6" stroke-width="0.9"/></svg>
        <span>dennis@qovo.com.au</span>
      </li>
      <li class="contacts__item">
        <svg class="contacts__icon" viewBox="0 0 12 12" aria-hidden="true"><path d="M6 0.5a4 4 0 0 0-4 4c0 3 4 7 4 7s4-4 4-7a4 4 0 0 0-4-4zm0 2.3a1.7 1.7 0 1 1 0 3.4 1.7 1.7 0 0 1 0-3.4z"/></svg>
        <span>P.O. Box 872 Kelvindale QLD 4309</span>
      </li>
    </ul>

    <div class="brand">
      <span class="brand__dot"></span>
      <span class="brand__name">Qovo International</span>
    </div>
  </section>
</main>
</body>
</html>
```